Business Card Design Project

I would like to have a project of business card with incorporated attachted logo elements in warm colors like: gold, yellow, brown.
We would like incorporate below information into the design
Name of the Company: Continental Hoop Invitational
Name: Dorian Pelkey
Position: Project Director
e-mail: dorian@hoopinvitational.net
mobile: +65 83147092
website: www.hoopinvitational.net
Address: 47 Marbury Lane, #06-11, Singapore 915274
There is a picture attachted which can be used as a back side of the buisness card - we would like to follow the colors theme on the front card ( with the person contact details) how ever the front card we will prefer with white background but with graphfic elements coming from logo.
Project Deadline Extended
Reason: the project has been launched on 24 of April with deadline by 24 of April by mistakes. Thats why I would like to extend the deadline.
Name: Dorian Pelkey
mobile: +65 83147092

```html
<!DOCTYPE html>
<html lang="en">
<head>
<meta charset="utf-8">
<title>Continental Hoop Invitational – Business Card</title>
<link rel="stylesheet" href="https://fonts.googleapis.com/css2?family=Fira+Sans:ital,wght@0,400;0,500;1,500&display=swap">
<style>
  :root {
    --stage: #ece8e1;
    --card-white: #ffffff;
    --yellow-light: #ddd35c;
    --yellow-deep: #d2bb2c;
    --khaki: #b49c5e;
    --ink: #1d1b16;
    --brand: #5c2c86;
    --back-dark: #1c140c;
    --back-brown: #4a3418;
    --back-gold: #c9a21c;
  }
  * { box-sizing: border-box; margin: 0; padding: 0; }
  html, body {
    width: 1200px; height: 900px; overflow: hidden;
    background: var(--stage);
    font-family: "Fira Sans", Arial, sans-serif;
    color: var(--ink);
  }
  .stage {
    position: relative; width: 1200px; height: 900px;
  }
  .card {
    position: absolute; top: 300px;
    width: 530px; height: 300px;
    box-shadow: 0 10px 28px rgba(0,0,0,.22);
    overflow: hidden;
  }
  .card--front { left: 40px; background: var(--card-white); }
  .card--back { left: 630px; }

  .front-bands { position: absolute; inset: 0; }
  .holder { position: absolute; left: 20px; top: 30px; }
  .holder__name { font-size: 19px; font-style: italic; font-weight: 500; }
  .holder__role { font-size: 14px; margin-left: 46px; margin-top: 1px; }

  .online {
    position: absolute; right: 20px; top: 108px;
    text-align: right; font-size: 14.5px; line-height: 17px;
  }
  .postal {
    position: absolute; right: 20px; top: 204px;
    font-size: 13.5px; line-height: 21px; font-weight: 500;
  }
  .postal__mobile { text-align: right; }

  .brand {
    position: absolute; left: 40px; top: 185px;
    display: flex; align-items: center; gap: 12px;
    width: 240px;
  }
  .brand__dot {
    flex: none; width: 34px; height: 34px; border-radius: 50%;
    background: var(--brand);
  }
  .brand__name {
    font-size: 21px; line-height: 23px; font-weight: 500;
    color: var(--brand);
    text-transform: uppercase;
  }

  .back-visual {
    position: absolute; inset: 0;
    background:
      radial-gradient(ellipse 45% 70% at 88% 65%, var(--back-gold) 0%, rgba(201,162,28,.55) 45%, rgba(201,162,28,0) 75%),
      radial-gradient(ellipse 40% 60% at 30% 45%, var(--back-brown) 0%, rgba(74,52,24,0) 80%),
      var(--back-dark);
  }
</style>
</head>
<body>
<main class="stage">

  <section class="card card--front" aria-label="Business card front">
    <svg class="front-bands" width="530" height="300" viewBox="0 0 530 300" aria-hidden="true">
      <polygon points="60,0 530,0 530,205 430,178" fill="var(--yellow-light)"/>
      <polygon points="350,150 530,108 530,205 430,178" fill="var(--yellow-deep)"/>
      <polygon points="170,300 530,198 530,300" fill="var(--khaki)"/>
    </svg>

    <div class="holder">
      <p class="holder__name">Dorian Pelkey</p>
      <p class="holder__role">Project Director</p>
    </div>

    <div class="online">
      <p>dorian@hoopinvitational.net</p>
      <p>www.hoopinvitational.net</p>
    </div>

    <div class="postal">
      <p class="postal__mobile">Mobile: +65 83147092</p>
      <p>47 Marbury Lane, #06-11,</p>
      <p>Singapore 915274</p>
    </div>

    <div class="brand">
      <span class="brand__dot" aria-hidden="true"></span>
      <p class="brand__name">Continental Hoop Invitational</p>
    </div>
  </section>

  <section class="card card--back" aria-label="Business card back">
    <div class="back-visual" role="img"
         aria-label="Photograph of a performer on a gold vertical pole over a dark brown background with a large faint brand emblem and a gold glow"></div>
  </section>

</main>
</body>
</html>
```